Lantern Holdings Business Card

We are looking to design new business cards for our company. We have two office locations and would like to have both full addresses on the card. Each address needs two lines for the building name and street address and a line or two for the city, state and zip code. There should be a place for 2-3 phone numbers. The addresses and phone numbers are at the bottom of this description. We also need a place to put our company website and one email address. Our logo is attached.
We would like the card to be two sided. The back of the card should have a blue background with some part of our logo design on it. We would like the full logo on the front of the card as well. The front of the card should have a white background with the blue logo. We are open to listing our addresses on the front or the back of the card. The person who designed our logo gave us an excellent business card idea that we really liked. I have attached a picture of his business card idea so that we can build off of it.
Addresses:
The Marlow Exchange
2214 47th Street NW
Washington, DC 20419
Osprey Harbor Tower
815 Tamsin Boulevard #2207
Miami, FL 33987
Phone Numbers: (202) 555-0148
(202) 555-0193
Website: www.lanternholdings-example.com

```html
<!DOCTYPE html>
<html lang="en">
<head>
<meta charset="utf-8">
<title>Lantern Holdings Business Card</title>
<link rel="stylesheet" href="https://fonts.googleapis.com/css2?family=Source+Sans+3:wght@400;600&display=swap">
<style>
  :root {
    --stage: #2b2b2d;
    --brand-blue: #1e2a9c;
    --brand-blue-deep: #141d78;
    --brand-blue-light: #2a37b4;
    --paper: #ffffff;
    --paper-shade: #e6e6ea;
    --text-light: #eef0fb;
    --faint-mark: rgba(255,255,255,0.07);
  }
  * { box-sizing: border-box; margin: 0; padding: 0; }
  html, body {
    width: 1200px; height: 900px; overflow: hidden;
    background: var(--stage);
    font-family: "Source Sans 3", "Myriad Pro", sans-serif;
  }
  .canvas { position: relative; width: 1200px; height: 900px; }
  .card {
    position: absolute; left: 250px; width: 700px; height: 400px;
    overflow: hidden; box-shadow: 0 10px 30px rgba(0,0,0,0.5);
  }
  .card-back {
    top: 35px;
    background: linear-gradient(135deg, var(--brand-blue-light) 0%, var(--brand-blue) 55%, var(--brand-blue-deep) 100%);
  }
  .card-back .faint-mark {
    position: absolute; right: 60px; top: 40px;
    width: 230px; height: 230px; border-radius: 50%;
    background: var(--faint-mark);
  }
  .card-back .brand {
    position: absolute; left: 150px; top: 235px;
    color: var(--text-light);
  }
  .brand-name {
    font-weight: 400; text-transform: uppercase;
    letter-spacing: 0.12em; line-height: 1; white-space: nowrap;
  }
  .card-back .brand-name { font-size: 38px; }
  .card-back .website {
    margin-top: 12px; font-size: 17px; letter-spacing: 0.03em;
  }
  .card-front { top: 465px; background: linear-gradient(180deg, var(--paper) 0%, var(--paper-shade) 100%); }
  .card-front svg.shape { position: absolute; inset: 0; }
  .card-front .brand-name {
    position: absolute; left: 200px; top: 70px;
    font-size: 30px; color: var(--brand-blue);
  }
  .office {
    position: absolute; color: var(--text-light);
    font-size: 16px; line-height: 1.22; font-style: normal;
  }
  .office .building { font-weight: 600; }
  .office-dc { left: 40px; top: 268px; }
  .office-miami { left: 440px; top: 190px; }
</style>
</head>
<body>
<main class="canvas">
  <section class="card card-back" aria-label="Card back">
    <div class="faint-mark" aria-hidden="true"></div>
    <div class="brand">
      <p class="brand-name">Lantern Holdings</p>
      <p class="website">www.lanternholdings-example.com</p>
    </div>
  </section>

  <section class="card card-front" aria-label="Card front">
    <svg class="shape" width="700" height="400" viewBox="0 0 700 400" aria-hidden="true">
      <defs>
        <linearGradient id="frontBlue" x1="0" y1="0" x2="1" y2="1">
          <stop offset="0" stop-color="#2a37b4"/>
          <stop offset="1" stop-color="#141d78"/>
        </linearGradient>
      </defs>
      <path d="M0,235 C260,235 480,190 700,75 L700,400 L0,400 Z" fill="url(#frontBlue)"/>
      <path d="M290,212 C430,202 520,170 600,108 C530,176 430,206 290,212 Z" fill="#1e2a9c"/>
    </svg>
    <p class="brand-name">Lantern Holdings</p>
    <address class="office office-dc">
      <span class="building">The Marlow Exchange</span><br>
      2214 47th Street NW<br>
      Washington, DC 20419<br>
      P: (202) 555-0148<br>
      P: (202) 555-0193<br>
      info1@lanternholdings-example.com
    </address>
    <address class="office office-miami">
      <span class="building">Osprey Harbor Tower</span><br>
      815 Tamsin Boulevard #2207<br>
      Miami, FL 33987<br>
      P: (202) 555-0148<br>
      P: (202) 555-0193<br>
      info2@lanternholdings-example.com
    </address>
  </section>
</main>
</body>
</html>
```